DESIGN A LEAFLET FOR A CANNABIS CLUB!!

We need a leaflet design for a cannabis club based in the United Kingdom, called Silver Pond Cannabis Club

PLEASE, FEEL FREE TO ADD YOUR OWN INFO ETC

Just want attention drawn to the INSTAGRAM/WEBSITE whilst looking semi-professional

LEGALIZE IT (title)

Government officials are denying your right to access legal Cannabis.

Over Thirty-five countries already have legal access in one form or another... What are we waiting for ?

I'd ideally like the leaflet to be A6 size

"INSTAGRAM LOGO": Silverpondcannabisclub
*MUST SEE*
"FACEBOOK LOGO": Silverpondcannabisclub
WEB: www.silverpondcannabisclub-example.com

Check us out!
*Cannabis Discussion Forum*
*Weed related news*
*Awesome Documentaries*

Industry/Entity Type

Club

Requirements
Must have
• Please use my logo on leaflet somewhere, feel free to re-size it
• Back of leaflet to just have my cannabis logo in large with green and smoky background
Nice to have
• PLEASE, FEEL FREE TO ADD YOUR OWN INFO ETC
• Just want attention drawn to INSTAGRAM/WEBSITE whilst looking semi-professional
Should not have
• Plain, boring, minimal effort

```html
<!DOCTYPE html>
<html lang="en">
<head>
<meta charset="utf-8">
<title>Silver Pond Cannabis Club – Leaflet</title>
<link href="https://fonts.googleapis.com/css2?family=Didact+Gothic&family=Montserrat:wght@700;800&display=swap" rel="stylesheet">
<style>
  :root{
    --stage:#b9b9b9;
    --brown:#7b5a3d;
    --green:#1f9a48;
    --grey:#8c8c8c;
    --text:#3d3d3d;
    --paper:#f6f8f4;
    --paper-tint:#e6ede4;
    --forest-1:#0d1710;
    --forest-2:#34503a;
    --forest-3:#1f3324;
    --sky:#e3eef4;
    --leaf-light:#9cc27a;
    --leaf-mid:#5f8f3e;
    --leaf-dark:#3f6a2c;
    --soil:#6e5a3c;
    --white:#ffffff;
  }
  *{box-sizing:border-box;margin:0;padding:0}
  html,body{width:1200px;height:806px;overflow:hidden}
  body{background:var(--stage);font-family:"Didact Gothic",sans-serif;color:var(--text);position:relative}

  .leaflet{position:absolute;top:201px;width:570px;height:404px;overflow:hidden;box-shadow:0 6px 18px rgba(0,0,0,.25)}
  .leaflet--back{left:20px}
  .leaflet--front{left:610px;background:var(--paper)}

  /* back */
  .back-scene{position:absolute;inset:0;
    background:
      radial-gradient(ellipse 45% 40% at 55% 60%,rgba(80,110,70,.55) 0%,rgba(80,110,70,0) 100%),
      radial-gradient(ellipse 60% 50% at 30% 80%,var(--forest-3) 0%,rgba(31,51,36,0) 100%),
      radial-gradient(ellipse at 50% 50%,var(--forest-2) 0%,var(--forest-1) 78%)}
  .back-brand{position:absolute;left:0;right:0;top:120px;display:flex;flex-direction:column;align-items:center;gap:18px}
  .back-brand .brand-dot{width:84px;height:84px;border-radius:50%;background:var(--green)}
  .back-brand .brand-name{font-size:40px;color:var(--white);text-align:center;line-height:1.15;width:420px}

  /* front: info panel */
  .info{position:absolute;left:0;top:0;width:398px;height:404px}
  .info-pattern{position:absolute;inset:0;background:linear-gradient(160deg,var(--paper) 0%,var(--paper-tint) 100%)}
  .title{position:absolute;left:26px;top:26px;font-family:"Montserrat",sans-serif;font-weight:800;font-size:40px;line-height:1;color:var(--brown);letter-spacing:.5px}
  .title .accent{color:var(--green)}
  .slogan{position:absolute;left:26px;top:74px;font-size:22px;line-height:1;color:var(--grey);font-variant:small-caps;letter-spacing:.5px}
  .slogan .accent{color:var(--green);font-weight:700}
  .body{position:absolute;left:26px;top:106px;width:330px;font-size:15.5px;line-height:1.28;color:var(--text)}
  .body p+p{margin-top:5px}
  .body .ask{display:block;font-family:"Montserrat",sans-serif;font-weight:700;color:var(--brown);font-size:14.5px}
  .shot{position:absolute;top:226px;height:66px;border:3px solid var(--green)}
  .shot--jars{left:26px;width:160px;border-color:var(--brown);background:linear-gradient(180deg,#4e3f2e 0%,#8d7a5e 55%,#5c4b37 100%)}
  .shot--bags{left:202px;width:168px;background:linear-gradient(180deg,#c2b196 0%,#9c8667 60%,#7f6d55 100%)}
  .checkout{position:absolute;left:26px;top:300px;font-family:"Montserrat",sans-serif;font-weight:800;font-size:21px;line-height:1;color:var(--brown)}
  .features{position:absolute;left:26px;top:328px;list-style:none;display:grid;grid-template-columns:auto auto;column-gap:18px;row-gap:3px;font-size:11.5px;line-height:1.2}
  .features li{display:flex;align-items:center;gap:5px;white-space:nowrap}
  .features svg{width:9px;height:9px;flex:none}
  .social-band{position:absolute;left:0;bottom:0;width:398px;height:32px;background:var(--brown);display:flex;align-items:center;gap:20px;padding-left:22px;color:var(--white);font-size:12px}
  .social-band span{display:flex;align-items:center;gap:6px;white-space:nowrap}
  .social-band i{width:14px;height:14px;border-radius:50%;background:var(--white);display:inline-block}

  .stripe{position:absolute;left:398px;top:0;width:10px;height:404px;background:var(--green)}

  /* front: photo panel */
  .photo{position:absolute;left:408px;top:0;width:162px;height:404px;
    background:
      radial-gradient(ellipse 70% 25% at 70% 48%,rgba(156,194,122,.9) 0%,rgba(156,194,122,0) 100%),
      radial-gradient(ellipse 60% 20% at 30% 90%,rgba(110,90,60,.55) 0%,rgba(110,90,60,0) 100%),
      linear-gradient(180deg,var(--sky) 0%,var(--sky) 22%,var(--leaf-light) 38%,var(--leaf-dark) 55%,var(--leaf-mid) 72%,var(--leaf-dark) 100%)}
  .photo-brand{position:absolute;left:408px;top:22px;width:162px;display:flex;flex-direction:column;align-items:center;gap:8px}
  .photo-brand .brand-dot{width:34px;height:34px;border-radius:50%;background:var(--green)}
  .photo-brand .brand-name{font-size:17px;color:var(--brown);text-align:center;line-height:1.15;width:130px}
  .web{position:absolute;left:412px;bottom:12px;width:156px;display:flex;align-items:center;gap:3px;font-size:7.2px;color:var(--white);white-space:nowrap}
  .web svg{width:9px;height:9px;flex:none}
</style>
</head>
<body>

<section class="leaflet leaflet--back">
  <div class="back-scene" role="img" aria-label="Dark misty pine forest background"></div>
  <div class="back-brand">
    <span class="brand-dot"></span>
    <span class="brand-name">Silver Pond Cannabis Club</span>
  </div>
</section>

<section class="leaflet leaflet--front">
  <div class="info">
    <div class="info-pattern" role="img" aria-label="Faint pale paisley pattern background"></div>
    <h1 class="title">LEGALIZE <span class="accent">IT</span></h1>
    <p class="slogan">“Save <span class="accent">Trees</span> Save World”</p>
    <div class="body">
      <p>Government officials are denying your right to access legal Cannabis.</p>
      <p>Over Thirty-five countries already have legal access in one form or another… <span class="ask">What are we waiting for ?</span></p>
    </div>
    <div class="shot shot--jars" role="img" aria-label="Photo of cannabis jars on a shop shelf"></div>
    <div class="shot shot--bags" role="img" aria-label="Photo of labelled cannabis bags on a table"></div>
    <h2 class="checkout">Check us out!</h2>
    <ul class="features">
      <li><svg viewBox="0 0 10 10"><path d="M1 5l3 3 5-7" fill="none" stroke="#7b5a3d" stroke-width="2"/></svg>Cannabis Discussion Forum</li>
      <li><svg viewBox="0 0 10 10"><path d="M1 5l3 3 5-7" fill="none" stroke="#7b5a3d" stroke-width="2"/></svg>Weed related news</li>
      <li><svg viewBox="0 0 10 10"><path d="M1 5l3 3 5-7" fill="none" stroke="#7b5a3d" stroke-width="2"/></svg>Awesome Documentaries</li>
    </ul>
    <div class="social-band">
      <span><i></i>Silverpondcannabisclub</span>
      <span><i></i>Silverpondcannabisclub</span>
    </div>
  </div>

  <div class="stripe"></div>

  <div class="photo" role="img" aria-label="Photo of two children watering a young tree in a green meadow"></div>
  <div class="photo-brand">
    <span class="brand-dot"></span>
    <span class="brand-name">Silver Pond Cannabis Club</span>
  </div>
  <div class="web">
    <svg viewBox="0 0 10 10"><circle cx="5" cy="5" r="4.2" fill="none" stroke="#fff"/><path d="M.8 5h8.4M5 .8c-2.4 2.6-2.4 5.8 0 8.4M5 .8c2.4 2.6 2.4 5.8 0 8.4" fill="none" stroke="#fff" stroke-width=".7"/></svg>
    www.silverpondcannabisclub-example.com
  </div>
</section>

</body>
</html>
```